Renata Quisby

Luxury And Style -

Black - White & Gold

Target Market(s)

Fashion

Industry/Entity Type

Fashion

Requirements
Must have
• High-End
Nice to have
• We will Print on Silk Paper

```html
<!DOCTYPE html>
<html lang="en">
<head>
<meta charset="utf-8">
<title>Renata Quisby – Letterhead</title>
<link rel="stylesheet" href="https://fonts.googleapis.com/css2?family=Roboto:wght@400&display=swap">
<style>
  :root {
    --paper: #ffffff;
    --ink: #111111;
    --text: #333333;
    --rule: #3a3a3a;
    --watermark: #ebebeb;
  }
  html, body {
    margin: 0;
    padding: 0;
    overflow: hidden;
    background: var(--paper);
  }
  .letterhead {
    position: relative;
    width: 856px;
    height: 1200px;
    background: var(--paper);
    overflow: hidden;
    font-family: "Roboto", sans-serif;
  }
  .brand {
    position: absolute;
    left: 78px;
    top: 118px;
    margin: 0;
    font-size: 30px;
    font-weight: 400;
    line-height: 1;
    color: var(--ink);
    white-space: nowrap;
  }
  .contact {
    position: absolute;
    left: 565px;
    top: 72px;
    font-style: normal;
    font-size: 17px;
    color: var(--text);
    line-height: 22px;
  }
  .contact-address {
    margin: 0 0 7px;
  }
  .contact-list {
    list-style: none;
    margin: 0;
    padding: 0;
  }
  .contact-list li {
    display: flex;
    align-items: center;
    gap: 6px;
    height: 23.5px;
  }
  .contact-icon {
    width: 16px;
    height: 16px;
    flex: none;
  }
  .header-rule {
    position: absolute;
    left: 78px;
    top: 216px;
    width: 713px;
    height: 0;
    margin: 0;
    border: 0;
    border-top: 1.5px solid var(--rule);
  }
  .watermark {
    position: absolute;
    left: 0;
    top: 585px;
    width: 856px;
    text-align: center;
    font-size: 96px;
    font-weight: 400;
    color: var(--watermark);
    line-height: 1;
    white-space: nowrap;
  }
</style>
</head>
<body>
<main class="letterhead">
  <header>
    <p class="brand">Renata Quisby</p>

    <address class="contact">
      <p class="contact-address">Lindenhofstr. 42<br>80469 Munich</p>
      <ul class="contact-list">
        <li>
          <svg class="contact-icon" viewBox="0 0 16 16" aria-hidden="true">
            <rect x="0.5" y="0.5" width="15" height="15" rx="2" fill="var(--ink)"/>
          </svg>
          <span>renataquisby.atelier</span>
        </li>
        <li>
          <svg class="contact-icon" viewBox="0 0 16 16" aria-hidden="true">
            <rect x="0.75" y="3" width="14.5" height="10" fill="none" stroke="var(--ink)" stroke-width="1.4"/>
            <path d="M1 3.5 L8 9 L15 3.5 M1 12.5 L6 7.8 M15 12.5 L10 7.8" fill="none" stroke="var(--ink)" stroke-width="1.2"/>
          </svg>
          <span>Info@Renata-Quisby.com</span>
        </li>
        <li>
          <svg class="contact-icon" viewBox="0 0 16 16" aria-hidden="true">
            <g fill="none" stroke="var(--ink)" stroke-width="1">
              <circle cx="8" cy="8" r="7"/>
              <ellipse cx="8" cy="8" rx="3" ry="7"/>
              <line x1="8" y1="1" x2="8" y2="15"/>
              <line x1="1" y1="8" x2="15" y2="8"/>
              <path d="M2.2 4.5 H13.8 M2.2 11.5 H13.8"/>
            </g>
          </svg>
          <span>www.renata-Quisby.com</span>
        </li>
      </ul>
    </address>
  </header>

  <hr class="header-rule">

  <div class="watermark" aria-hidden="true">Renata Quisby</div>
</main>
</body>
</html>
```